Marrowind Leaf range - labels for a range of teas.

Our company name is Marrowind Leaf Company - based in Melbourne, Australia. We have a current logo project with Pixel Harbor.

We offer a range of top quality teas - black, green, white, oolongs, herbals, flavoured teas. From Japan, Assam, Darjeeling, Ceylon, Africa and elsewhere. The very best loose teas, and some pyramid tea bags too.

We cover some blends : English Breakfast, African Breakfast, Ceylon Breakfast, Earl Grey amongst them.

And herbal variants: lemon grass and ginger, chamomile, peppermint, rooibos and chilli.

And fruit teas.... and flavoured teas like vanilla, peach and raspberry.

We aim to occupy a modern, contemporary, sophisticated and global space.... but we can be funky too, especially with the fruit and herbal offers. Quality is paramount ! We do not aim to have the biggest range of teas, but we are very particular. And we source directly from origin.... fresh quality teas.

Would lean towards black teas being on a black background label, green teas on a green background, white etas on a white background, herbals maybe on a straw or suitable background, and flavoured teas on a specific background colour too....maybe fuschia? Violet ? But colourful is key.

The panel should indicate teas being Loose or Pyramid bags. And the nett weight should be shown.... Loose could be for example 75 gr, 125 gr 250 gr etc.. And pyramids would show the number of pyramids and weight, example 20 x Pyramids 50 gr
50 Pyramids 150 gr etc.

And 'Marrowind Leaves' or 'Marrowind Leaf Company' should be on the panel too. Melbourne can appear as well if it gels with the total look.

There will need to be 2 lines - in order or juxtaposed, doesn't matter - showing the origin and 'mark' and grade. Example being:
Ceylon
Kenwick Pekoe

or

Darjeeling
Melgara TGFOP1

or

China
Jasmine Leaf

We just need templates to cover the different types of tea - black, green, white, herbal, flavoured - as there are too many (and changing) types of tea in the range .

Any questions...please ask...

Thanks

Reason: Needs to have alater deadline than the current Logo Project associated with the same Marrowind Leaf Company start up.

Target Market(s)

Sophisticated. Real tea lovers. Discriminating tastes.

Industry/Entity Type

Weight

Font styles to use
Sans Serif

Requirements
Must have
• Sophisticated
Cool
Premium quality branding
Bold
Uber modern
Nice to have
• BOLD text.....
Cool fonts....
Pretty bold and minimalist - ultra modern if possible....uber modern
Bright colours and use of black and white..... Not really into pastels etc..

Lots of black colour too is a likely plus
Should not have
• Frilly stuff

```html
<!DOCTYPE html>
<html lang="en">
<head>
<meta charset="utf-8">
<title>Marrowind Leaf — Tea Label Range</title>
<link rel="stylesheet" href="https://fonts.googleapis.com/css2?family=Arimo:wght@400;700&display=swap">
<style>
  :root {
    --page: #ffffff;
    --label: #58585a;
    --white: #f2f2f2;
    --soft-grey: #b9b9b9;
    --herbal: #fff200;
    --green: #8dc63f;
    --flavoured: #d7df23;
    --oolong: #c6b99b;
    --rule-green: #8dc63f;
  }
  html, body {
    margin: 0;
    padding: 0;
    width: 1200px;
    height: 848px;
    overflow: hidden;
    background: var(--page);
  }
  .range {
    position: relative;
    width: 1200px;
    height: 848px;
    font-family: "Arimo", Helvetica, Arial, sans-serif;
  }
  .tea-label {
    position: absolute;
    width: 200px;
    height: 281px;
    display: block;
  }
  .tea-label .panel { fill: var(--label); }
  .tea-label .type-word { font-weight: 700; font-size: 56px; letter-spacing: -1px; }
  .tea-label .tea-word { font-weight: 700; font-size: 66px; fill: var(--white); letter-spacing: -1px; }
  .tea-label .origin { font-weight: 700; font-size: 24px; letter-spacing: -0.5px; }
  .tea-label .grade { font-weight: 700; font-size: 14px; }
  .tea-label .brand-name { font-weight: 700; font-size: 11px; fill: var(--green); }
  .tea-label .weight { font-weight: 700; font-size: 18px; fill: var(--white); }

  .label-black { left: 51px; top: 40px; }
  .label-herbal { left: 308px; top: 40px; }
  .label-white { left: 570px; top: 40px; }
  .label-green { left: 825px; top: 40px; }
  .label-flavoured { left: 51px; top: 364px; }
  .label-oolong { left: 311px; top: 364px; }
</style>
</head>
<body>
<main class="range">

  <svg class="tea-label label-black" viewBox="0 0 200 281" aria-label="Black tea label">
    <rect class="panel" width="200" height="281"/>
    <text class="type-word" fill="var(--soft-grey)" transform="translate(47,0) rotate(-90)" x="-3" text-anchor="end">Black</text>
    <text class="tea-word" x="199" y="54" text-anchor="end">TEA</text>
    <line x1="55" y1="76" x2="200" y2="76" stroke="var(--soft-grey)" stroke-width="1.5"/>
    <text class="origin" fill="var(--soft-grey)" x="55" y="112">Darjeeling</text>
    <text class="grade" fill="var(--soft-grey)" x="55" y="138">Melgara TGFOP1</text>
    <text class="brand-name" x="99" y="214" text-anchor="middle">Marrowind Leaf</text>
    <text class="weight" x="99" y="266" text-anchor="middle">125g</text>
  </svg>

  <svg class="tea-label label-herbal" viewBox="0 0 200 281" aria-label="Herbal tea label">
    <rect class="panel" width="200" height="281"/>
    <text class="type-word" fill="var(--herbal)" transform="translate(47,0) rotate(-90)" x="-3" text-anchor="end">Herbal</text>
    <text class="tea-word" x="199" y="54" text-anchor="end">TEA</text>
    <line x1="55" y1="76" x2="200" y2="76" stroke="var(--herbal)" stroke-width="1.5"/>
    <text class="origin" fill="var(--herbal)" x="55" y="110" font-size="22">Chamomile</text>
    <text class="brand-name" x="99" y="214" text-anchor="middle">Marrowind Leaf</text>
    <text class="weight" x="99" y="266" text-anchor="middle">125g</text>
  </svg>

  <svg class="tea-label label-white" viewBox="0 0 200 281" aria-label="White tea label">
    <rect class="panel" width="200" height="281"/>
    <text class="type-word" fill="var(--white)" transform="translate(47,0) rotate(-90)" x="-3" text-anchor="end">White</text>
    <text class="tea-word" x="199" y="54" text-anchor="end">TEA</text>
    <line x1="55" y1="76" x2="200" y2="76" stroke="var(--white)" stroke-width="1.5"/>
    <text class="brand-name" x="99" y="214" text-anchor="middle">Marrowind Leaf</text>
    <text class="weight" x="99" y="266" text-anchor="middle">125g</text>
  </svg>

  <svg class="tea-label label-green" viewBox="0 0 200 281" aria-label="Green tea label">
    <rect class="panel" width="200" height="281"/>
    <text class="type-word" fill="var(--green)" transform="translate(47,0) rotate(-90)" x="-3" text-anchor="end">Green</text>
    <text class="tea-word" x="199" y="54" text-anchor="end">TEA</text>
    <line x1="55" y1="76" x2="200" y2="76" stroke="var(--rule-green)" stroke-width="1.5"/>
    <text class="brand-name" x="99" y="214" text-anchor="middle">Marrowind Leaf</text>
    <text class="weight" x="99" y="266" text-anchor="middle">125g</text>
  </svg>

  <svg class="tea-label label-flavoured" viewBox="0 0 200 281" aria-label="Flavoured tea label">
    <rect class="panel" width="200" height="281"/>
    <text class="type-word" fill="var(--flavoured)" transform="translate(47,0) rotate(-90)" x="-3" text-anchor="end" textLength="270" lengthAdjust="spacingAndGlyphs">Flavoured</text>
    <text class="tea-word" x="199" y="54" text-anchor="end">TEA</text>
    <line x1="55" y1="76" x2="200" y2="76" stroke="var(--flavoured)" stroke-width="1.5"/>
    <text class="brand-name" x="99" y="214" text-anchor="middle">Marrowind Leaf</text>
    <text class="weight" x="99" y="266" text-anchor="middle">125g</text>
  </svg>

  <svg class="tea-label label-oolong" viewBox="0 0 200 281" aria-label="Oolong tea label">
    <rect class="panel" width="200" height="281"/>
    <text class="type-word" fill="var(--oolong)" transform="translate(47,0) rotate(-90)" x="-3" text-anchor="end">Oolong</text>
    <text class="tea-word" x="199" y="54" text-anchor="end">TEA</text>
    <line x1="55" y1="76" x2="200" y2="76" stroke="var(--oolong)" stroke-width="1.5"/>
    <text class="brand-name" x="99" y="214" text-anchor="middle">Marrowind Leaf</text>
    <text class="weight" x="99" y="266" text-anchor="middle">125g</text>
  </svg>

</main>
</body>
</html>
```